Web Design Project!!

This is the clients current site: http://brantorhomegoods.example/
I want this new design to be AMAZING! I think the current site looks fine, but the client is wanting a lot of new features added to the site so will need a new design. I need a home page design and a simple internal page also. Social media is one of the most important features of the site. Contact me with any questions. I am really just letting you all flow with this project. If you look at the clients show office location, you will see it looks amazing!
I have attached the proposal of features that are going to be needed in the site and page names.
Industry/Entity Type
Media
Look and feel
Each slider illustrates characteristics of the customer's brand and the style your logo design should communicate.

```html
<!DOCTYPE html>
<html lang="en">
<head>
<meta charset="utf-8">
<title>Brantor Home Goods</title>
<link href="https://fonts.googleapis.com/css2?family=Arimo:wght@400;700&display=swap" rel="stylesheet">
<style>
:root{
  --green:#7cc01f;
  --green-dark:#5f9a12;
  --blue:#1f9ad6;
  --blue-dark:#137bb0;
  --ink:#222;
  --text:#444;
  --muted:#777;
  --panel:#f0f0f0;
  --rule:#c9c9c9;
  --charcoal:#2c2c2c;
  --coal:#1e1e1e;
  --white:#fff;
}
*{box-sizing:border-box;margin:0;padding:0}
html,body{width:673px;height:1200px;overflow:hidden;background:var(--white)}
body{font-family:"Arimo",Arial,sans-serif;color:var(--text);font-size:8px;line-height:1.35}
.page{position:relative;width:673px;height:1200px;overflow:hidden}
.abs{position:absolute}
.photo{position:absolute;border-radius:2px}

/* header */
.site-header{position:absolute;left:0;top:0;width:673px;height:56px;background:linear-gradient(#fff,#f1f1f1)}
.brand{position:absolute;left:94px;top:14px;display:flex;align-items:center;gap:6px}
.brand-mark{width:14px;height:14px;background:var(--ink)}
.brand-name{font-weight:700;font-size:15px;color:var(--ink);letter-spacing:.5px}
.contact-mail{position:absolute;left:438px;top:9px;display:flex;align-items:center;gap:5px;font-size:11px;font-weight:700;color:var(--ink);text-decoration:underline}
.main-nav{position:absolute;left:284px;top:33px;display:flex;gap:3px}
.main-nav a{font-size:8px;color:var(--text);text-decoration:none;padding:3px 5px}
.main-nav a.active{background:var(--blue);color:var(--white)}

/* hero */
.hero{position:absolute;left:0;top:56px;width:673px;height:160px;background:radial-gradient(circle at 25% 40%,#93d335,var(--green) 45%,var(--green-dark))}
.hero-title{position:absolute;left:83px;top:32px;font-size:19px;font-weight:700;color:var(--white)}
.hero-copy{position:absolute;left:85px;top:60px;width:190px;font-size:9px;color:var(--white)}
.btn-learn{position:absolute;left:84px;top:108px;background:var(--blue);color:var(--white);font-size:10px;padding:4px 6px;border:1px solid #fff}
.slider{position:absolute;left:285px;top:12px;width:305px;height:138px;border:3px solid var(--white);background:linear-gradient(135deg,#6b4427,#c8955d 45%,#e8d3b2 70%,#7a5534)}
.slider-arrow{position:absolute;top:50px;width:15px;height:22px;background:var(--white);display:flex;align-items:center;justify-content:center}
.slider-dots{position:absolute;right:6px;bottom:5px;display:flex;gap:3px}
.slider-dots i{width:4px;height:4px;border-radius:50%;background:#fff;opacity:.7}

/* promo bar */
.promo-bar{position:absolute;left:0;top:216px;width:673px;height:25px;background:var(--charcoal)}
.follow{position:absolute;left:88px;top:6px;font-size:10px;font-weight:700;color:var(--white);display:flex;align-items:center;gap:4px}
.follow span.icon{width:12px;height:12px;background:var(--blue)}
.claim{position:absolute;left:278px;top:6px;font-size:11px;font-weight:700;color:#3cb4ea}

/* ribbons */
.ribbon{position:absolute;height:21px;color:var(--white);font-size:10px;font-weight:700;line-height:21px;padding-left:8px;white-space:nowrap;background:var(--blue);clip-path:polygon(0 0,calc(100% - 9px) 0,100% 50%,calc(100% - 9px) 100%,0 100%)}
.ribbon.green{background:var(--green)}

/* feature section */
.features{position:absolute;left:0;top:241px;width:673px;height:207px;background:linear-gradient(#fafafa,#e9e9e9)}
.video-frame{position:absolute;left:91px;top:55px;width:184px;height:118px;border:3px solid #ddd;background:linear-gradient(#4c5d3a,#8a8d7a 60%,#3c3c3c)}
.play{position:absolute;left:78px;top:42px;width:28px;height:22px;background:rgba(0,0,0,.75);display:flex;align-items:center;justify-content:center}
.view-more{position:absolute;left:150px;top:186px;font-size:9px;color:var(--ink)}
.feature-title{position:absolute;left:322px;font-size:11px;font-weight:700;color:var(--ink)}
.feature-copy{position:absolute;left:322px;width:150px;font-size:7.5px;color:var(--text)}
.btn-more{position:absolute;left:322px;background:var(--blue);color:var(--white);font-size:7px;padding:2px 5px}
.dash{position:absolute;border-top:1px dashed var(--rule)}

/* lists */
.lists{position:absolute;left:0;top:448px;width:673px;height:253px;background:linear-gradient(#f4f4f4,#e2e2e2)}
.item-title{position:absolute;font-size:8px;font-weight:700;color:var(--ink)}
.item-copy{position:absolute;width:165px;font-size:7px}
.item-meta{position:absolute;font-size:6.5px;color:var(--muted)}
.item-meta b{color:var(--blue);font-weight:400}

/* testimonials */
.social{position:absolute;left:0;top:701px;width:673px;height:186px;background:var(--white)}
.quote{position:absolute;left:88px;width:166px;font-size:7px;line-height:1.3}
.quote-name{position:absolute;left:88px;font-size:8px;font-weight:700;color:var(--ink)}
.widget{position:absolute;top:20px;height:162px;border:1px solid #cfd6e4;background:#fff}
.widget-head{height:26px;background:#eef1f7;border-bottom:1px solid #cfd6e4;position:relative}
.avatars{position:absolute;left:6px;display:grid;grid-template-columns:repeat(5,24px);gap:3px 5px}
.avatars div{height:22px;background:#c7c9cc}
.avatars span{font-size:5px;color:var(--muted);display:block;margin-top:23px;white-space:nowrap}

/* gallery */
.gallery{position:absolute;left:83px;top:908px;width:507px;height:75px;background:linear-gradient(#e4e4e4,#cfcfcf);border:1px solid #bbb}
.gallery .thumb{position:absolute;top:8px;width:80px;height:60px;border:3px solid var(--white);background:linear-gradient(135deg,#8b3b16,#d86d2a 55%,#f1c08a)}

/* outdoor */
.outdoor{position:absolute;left:0;top:1016px;width:673px;height:125px;background:var(--charcoal)}
.partner-name{position:absolute;left:92px;top:10px;width:56px;height:15px;background:#2a4f8f;color:var(--white);font-size:8px;font-weight:700;line-height:15px;text-align:center}
.field{position:absolute;left:445px;width:140px;height:15px;background:var(--white);border:1px solid #999;font-size:6.5px;color:#555;padding:3px 4px}

/* footer */
.site-footer{position:absolute;left:0;top:1141px;width:673px;height:59px;background:var(--coal);color:#999;font-size:6.5px}
</style>
</head>
<body>
<div class="page">

  <header class="site-header">
    <div class="brand"><span class="brand-mark"></span><span class="brand-name">BRANTOR</span></div>
    <div class="contact-mail">
      <svg width="14" height="11" viewBox="0 0 14 11"><rect x=".5" y=".5" width="13" height="10" fill="#fff" stroke="#888"/><path d="M.5 .5 7 6 13.5 .5" fill="none" stroke="#888"/></svg>
      info@brantorhomegoods.example
    </div>
    <nav class="main-nav">
      <a class="active">Home</a><a>Company</a><a>Showroom</a><a>Brands</a><a>Gallery</a><a>Service</a><a>Directions</a><a>Contact</a>
    </nav>
  </header>

  <section class="hero">
    <h1 class="hero-title">The Living Kitchen</h1>
    <p class="hero-copy">Come visit our brand new location and view the new Living Kitchen showroom. It's an experience you won't forget!</p>
    <span class="btn-learn">Lern More</span>
    <div class="slider" role="img" aria-label="Showroom kitchen with wooden cabinets and steel appliances">
      <span class="slider-arrow" style="left:0"><svg width="6" height="9"><path d="M5 0 0 4.5 5 9" fill="none" stroke="#333" stroke-width="1.5"/></svg></span>
      <span class="slider-arrow" style="right:0"><svg width="6" height="9"><path d="M1 0 6 4.5 1 9" fill="none" stroke="#333" stroke-width="1.5"/></svg></span>
      <div class="slider-dots"><i></i><i></i><i></i><i></i><i></i><i></i></div>
    </div>
  </section>

  <div class="promo-bar">
    <div class="follow">Follow us on <span class="icon"></span><span class="icon" style="background:#3b5998"></span></div>
    <div class="claim">Claim $2500.00 Toward Remodeling, Ask How : 404-555-0199</div>
  </div>

  <section class="features">
    <div class="ribbon" style="left:88px;top:21px;width:192px">LATEST CLIPSTREAM VIDEO</div>
    <div class="video-frame" role="img" aria-label="Video still of the showroom building exterior">
      <span class="play"><svg width="9" height="10"><path d="M0 0 9 5 0 10z" fill="#fff"/></svg></span>
    </div>
    <div class="view-more">▸ VIEW MORE</div>

    <div class="feature-title" style="top:20px">Cooking Demonstrations</div>
    <p class="feature-copy" style="top:36px">Come see the art of cooking live in our fully furnished Living Kitchen. You will see step by step instructions on how to get the most out of your kitchen at home.</p>
    <span class="btn-more" style="top:78px">More info ▸</span>
    <div class="photo" style="left:480px;top:18px;width:105px;height:72px;border:3px solid #fff;background:linear-gradient(135deg,#f4f1ea,#c88e5a 60%,#7d3d1f)" role="img" aria-label="Chef presenting a plated dish"></div>
    <div class="dash" style="left:322px;top:102px;width:263px"></div>

    <div class="feature-title" style="top:115px">New Location</div>
    <p class="feature-copy" style="top:132px">Come visit our new showroom located at 1280 Alder Creek Road in Millbrook, GA.</p>
    <span class="btn-more" style="top:160px">More info ▸</span>
    <div class="photo" style="left:480px;top:115px;width:105px;height:55px;border:2px solid #fff;background:linear-gradient(135deg,#e8e4da,#d6dccd)" role="img" aria-label="Street map of the new showroom location"></div>
    <p class="feature-copy" style="top:176px;width:265px">Check out Falcrest Ovens live! Stop by Booth # 1035 at the 28th Annual Riverside Fall Home Show. Harbor Expo Hall September 23rd-25th riversidehomeshow.example</p>
  </section>

  <section class="lists">
    <div class="ribbon" style="left:83px;top:14px;width:150px">LATEST COOKING EVENTS</div>
    <div class="ribbon" style="left:348px;top:14px;width:142px">LATEST BLOG ARTICLES</div>

    <div class="photo" style="left:87px;top:42px;width:62px;height:42px;border:2px solid #fff;background:linear-gradient(135deg,#b4562a,#e3a56a)" role="img" aria-label="Kitchen display"></div>
    <div class="item-title" style="left:158px;top:43px">Lorem Ipsum is simpl</div>
    <p class="item-copy" style="left:158px;top:55px">Lorem Ipsum is simply dummy text of theprinting and typesetting industry. Lorem Ipsum has been the industry's standard dummy text ever since the 1500s</p>
    <div class="item-meta" style="left:163px;top:87px">** Read more</div>
    <div class="dash" style="left:85px;top:100px;width:238px"></div>

    <div class="photo" style="left:87px;top:117px;width:62px;height:42px;border:2px solid #fff;background:linear-gradient(135deg,#9e1f1f,#e0d8cc)" role="img" aria-label="Red kitchen interior"></div>
    <div class="item-title" style="left:158px;top:118px">Lorem Ipsum is simpl</div>
    <p class="item-copy" style="left:158px;top:130px">Lorem Ipsum is simply dummy text of theprinting and typesetting industry. Lorem Ipsum has been the industry's standard dummy text ever since the 1500s</p>
    <div class="item-meta" style="left:163px;top:162px">** Read more</div>
    <div class="dash" style="left:85px;top:175px;width:238px"></div>

    <div class="photo" style="left:87px;top:192px;width:62px;height:42px;border:2px solid #fff;background:linear-gradient(135deg,#6a2c12,#d49a5c)" role="img" aria-label="Wooden kitchen interior"></div>
    <div class="item-title" style="left:158px;top:193px">Lorem Ipsum is simpl</div>
    <p class="item-copy" style="left:158px;top:205px">Lorem Ipsum is simply dummy text of theprinting and typesetting industry. Lorem Ipsum has been the industry's standard dummy text ever since the 1500s</p>
    <div class="item-meta" style="left:163px;top:237px">** Read more</div>

    <div class="photo" style="left:352px;top:42px;width:62px;height:42px;border:2px solid #fff;background:linear-gradient(135deg,#d9dfe5,#8fa3b3)" role="img" aria-label="Staff member in showroom"></div>
    <div class="item-title" style="left:423px;top:43px">Lorem Ipsum is simpl</div>
    <p class="item-copy" style="left:423px;top:55px">Lorem Ipsum is simply dummy text of theprinting and typesetting industry. Lorem Ipsum has been the ...</p>
    <div class="item-meta" style="left:423px;top:82px">Posted by <b>Admin</b> | <b>23rd march</b></div>
    <div class="dash" style="left:350px;top:100px;width:240px"></div>

    <div class="photo" style="left:352px;top:117px;width:62px;height:42px;border:2px solid #fff;background:linear-gradient(135deg,#2c2a25,#a68a5e)" role="img" aria-label="Cooking demonstration"></div>
    <div class="item-title" style="left:423px;top:118px">Lorem Ipsum is simpl</div>
    <p class="item-copy" style="left:423px;top:130px">Lorem Ipsum is simply dummy text of theprinting and typesetting industry. Lorem Ipsum has been the ...</p>
    <div class="item-meta" style="left:423px;top:157px">Posted by <b>Admin</b> | <b>23rd march</b></div>
    <div class="dash" style="left:350px;top:175px;width:240px"></div>

    <div class="photo" style="left:352px;top:192px;width:62px;height:42px;border:2px solid #fff;background:linear-gradient(135deg,#7c1d1d,#d9c2a8)" role="img" aria-label="Dining room display"></div>
    <div class="item-title" style="left:423px;top:193px">Lorem Ipsum is simpl</div>
    <p class="item-copy" style="left:423px;top:205px">Lorem Ipsum is simply dummy text of theprinting and typesetting industry. Lorem Ipsum has been the ...</p>
    <div class="item-meta" style="left:423px;top:232px">Posted by <b>Admin</b> | <b>23rd march</b></div>
  </section>

  <section class="social">
    <div class="ribbon" style="left:83px;top:20px;width:150px">CLIENTS TESTIMONIALS</div>
    <p class="quote" style="top:50px">Lorem Ipsum is simply dummy text of theprinting and typesetting industry. Lorem Ipsum has been the industry's standard dummy text ever since the 1500s</p>
    <div class="quote-name" style="top:90px">L. Harper</div>
    <p class="quote" style="top:108px">Lorem Ipsum is simply dummy text of theprinting and typesetting industry. Lorem Ipsum has been the industry's standard dummy text ever since the 1500s</p>
    <div class="quote-name" style="top:150px">Daniel</div>

    <div class="widget" style="left:270px;width:156px">
      <div class="widget-head">
        <span class="abs" style="left:5px;top:5px;width:16px;height:12px;background:var(--ink)"></span>
        <span class="abs" style="left:25px;top:4px;font-size:6px;color:var(--ink)">Brantor Home Goods on Chirper</span>
        <span class="abs" style="left:42px;top:14px;font-size:5.5px;background:#ddd;padding:0 3px">Follow</span>
      </div>
      <div class="abs" style="left:6px;top:32px;font-size:6px;color:var(--ink)">Ravi Kell has 12 Followers</div>
      <div class="avatars" style="top:44px">
        <div><span>Bede</span></div><div><span>Jalil</span></div><div><span>Mara</span></div><div><span>Noor</span></div><div><span>Tess</span></div>
      </div>
      <div class="avatars" style="top:90px">
        <div><span>Luis</span></div><div><span>Ines</span></div><div><span>Omar</span></div><div><span>Kira</span></div><div><span>Paul</span></div>
      </div>
    </div>

    <div class="widget" style="left:433px;width:157px">
      <div class="widget-head">
        <span class="abs" style="left:5px;top:5px;width:16px;height:12px;background:var(--ink)"></span>
        <span class="abs" style="left:25px;top:3px;font-size:8px;color:#3b5998;font-weight:700">Brantor Home Goods</span>
        <span class="abs" style="left:25px;top:14px;font-size:5.5px;color:var(--muted)">on Friendbook</span>
      </div>
      <div class="abs" style="left:6px;top:32px;font-size:6px;color:var(--ink)">7,121 people like Brantor Home Goods</div>
      <div class="avatars" style="top:44px">
        <div><span>Nick</span></div><div><span>Jana</span></div><div><span>Eli</span></div><div><span>Adam</span></div><div><span>Lea</span></div>
      </div>
      <div class="avatars" style="top:90px">
        <div><span>Cara</span></div><div><span>Olive</span></div><div><span>Piet</span></div><div><span>Randy</span></div><div><span>Mike</span></div>
      </div>
    </div>
  </section>

  <section class="gallery" aria-label="Showroom gallery">
    <span class="abs" style="left:-2px;top:25px;width:12px;height:24px;background:#eee;border:1px solid #bbb"></span>
    <div class="thumb" style="left:22px" role="img" aria-label="Orange vaulted kitchen"></div>
    <div class="thumb" style="left:116px;background:linear-gradient(135deg,#5a4030,#c9b090)" role="img" aria-label="Open plan living kitchen"></div>
    <div class="thumb" style="left:210px" role="img" aria-label="Kitchen with orange ceiling"></div>
    <div class="thumb" style="left:304px;background:linear-gradient(135deg,#6b1a12,#c4553a)" role="img" aria-label="Red kitchen island"></div>
    <div class="thumb" style="left:398px;background:linear-gradient(135deg,#7b5a3a,#e6d2b2)" role="img" aria-label="Dining table display"></div>
    <span class="abs" style="right:-2px;top:25px;width:12px;height:24px;background:#eee;border:1px solid #bbb"></span>
  </section>

  <div class="ribbon green" style="left:88px;top:990px;width:190px">OUTDOOR GRILLING CLASSES</div>

  <section class="outdoor">
    <div class="partner-name">FALCREST</div>
    <div class="abs" style="left:154px;top:13px;font-size:7px;color:#3cb4ea;font-weight:700">WATCH THE 3-YEAR FALCREST SIGNATURE WARRANTY VIDEO</div>
    <div class="photo" style="left:92px;top:34px;width:140px;height:80px;border:2px solid #555;background:linear-gradient(135deg,#1d1d1d,#6d6658)" role="img" aria-label="Warranty video still">
      <span class="play" style="left:56px;top:29px"><svg width="9" height="10"><path d="M0 0 9 5 0 10z" fill="#fff"/></svg></span>
    </div>
    <div class="photo" style="left:236px;top:34px;width:56px;height:37px;background:linear-gradient(135deg,#5a4a3a,#b89a78)" role="img" aria-label="Outdoor grill area"></div>
    <div class="photo" style="left:296px;top:34px;width:56px;height:37px;background:linear-gradient(135deg,#7a2a1a,#c88a5a)" role="img" aria-label="Outdoor kitchen"></div>
    <div class="photo" style="left:356px;top:34px;width:56px;height:37px;background:linear-gradient(135deg,#3f5a30,#b8c39a)" role="img" aria-label="Patio grill setup"></div>
    <div class="photo" style="left:236px;top:77px;width:56px;height:37px;background:linear-gradient(135deg,#a2461e,#e7a060)" role="img" aria-label="Grilling class"></div>
    <div class="photo" style="left:296px;top:77px;width:56px;height:37px;background:linear-gradient(135deg,#4a3020,#caa27a)" role="img" aria-label="Outdoor dining area"></div>
    <div class="photo" style="left:356px;top:77px;width:56px;height:37px;background:linear-gradient(135deg,#6a4a2a,#d9c09a)" role="img" aria-label="Backyard kitchen"></div>

    <div class="abs" style="left:445px;top:12px;font-size:9px;color:var(--white)">Sign up to receive updates &amp; events</div>
    <div class="field" style="top:32px">Enter your name here</div>
    <div class="field" style="top:52px">Enter your email here</div>
    <span class="abs" style="left:445px;top:76px;background:var(--blue);color:#fff;font-size:8px;padding:2px 6px">Submit Now ▸</span>
  </section>

  <footer class="site-footer">
    <div class="abs" style="left:90px;top:16px">Home | Company | Showroom | Brands | Gallery | Service | Directions | Contact | Site Map</div>
    <div class="abs" style="left:90px;top:29px;color:var(--blue)">COPYRIGHT 2010 | BRANTOR HOME GOODS</div>
    <div class="abs" style="left:90px;top:40px;font-size:5.5px">1280 Alder Creek Rd. NE, Millbrook, GA 30320 | 404.555.0199 | Mon - Fri: 9:00am-6:00pm Sat: 10:00am-4:00pm</div>
    <span class="abs" style="left:452px;top:20px;width:34px;height:26px;background:#ddd;border:2px solid #2a4f8f"></span>
    <span class="abs" style="left:494px;top:28px;width:20px;height:12px;background:#ccc"></span>
    <span class="abs" style="left:517px;top:28px;width:20px;height:12px;background:#1a3a8a"></span>
    <span class="abs" style="left:540px;top:28px;width:20px;height:12px;background:#d8892a"></span>
    <span class="abs" style="left:563px;top:28px;width:20px;height:12px;background:#2a7ac0"></span>
  </footer>

</div>
</body>
</html>
```